New Template, new corporate image Quelmoro 2022

New template designs for google slides or PowerPoint. Match to new corporate image. The new website www.quelmoro-mx.com Needs to match our new version. Technology and Artificial Intelligence elements to reflect our type of work.
We are adding old version of template and will send elements for the new corporate images.
Please consider our website as the main corporate image.
Our templates are being used on customer presentations, webminars, internal work only.
We have our main name of company Quelmoro. Quelmoro has to be in all the templates.
Secondary logo or branded service is: Calvindar.

Target Market(s)

Industrial users. Asset managers. Corporate visitors and customers.

Industry/Entity Type

Automotive. Chemical. Food and Beverage. Manufacturing

Other font styles liked:
• GE INSPIRA. RALEWAY

Colors
0054AA
0677BA
7BADD7
CADEEF
E8F1F8

Requirements
Must have
• Match to our elements on the new image. Use Brain Icons. Chips icons to connect equipments with software and control. Innovation.
Nice to have
• Unique images, machine images. Connecting machines and data elements. Template version for google slides. Image for industrial software for control equipment and saving money to manufacturers. Segments: Automotive, Chemical, Food and Beverages, Mining and pharmaceutical, Energy Management
Should not have
• old elements. not to much images of medical devices. Do not seems like a hospital.

```html
<!DOCTYPE html>
<html lang="en">
<head>
<meta charset="utf-8">
<title>Quelmoro 2022 Presentation Template</title>
<link href="https://fonts.googleapis.com/css2?family=Raleway:wght@300;400;500;600;700&display=swap" rel="stylesheet">
<style>
:root{
  --navy:#0054AA;
  --blue:#0677BA;
  --sky:#7BADD7;
  --mist:#CADEEF;
  --ice:#E8F1F8;
  --bright:#2a8fd8;
  --ink:#1d2228;
  --grey:#7a7f86;
  --panel:#999b9e;
  --night:#061521;
}
*{margin:0;padding:0;box-sizing:border-box}
html,body{width:1200px;height:2178px;overflow:hidden}
body{font-family:"Raleway",sans-serif;background:var(--panel);position:relative;color:var(--ink)}
.hero{position:absolute;left:0;top:0;width:1200px;height:795px;background:linear-gradient(180deg,#d9dde3 0%,#c3c8cf 60%,#b5b9bf 100%)}
.hero .wordmark{position:absolute;right:95px;top:95px;font-size:42px;font-weight:500;color:var(--blue);letter-spacing:1px}
.hero .feature{position:absolute;left:220px;top:190px;width:760px;height:428px;overflow:hidden;box-shadow:0 20px 40px rgba(0,0,0,.25)}
.grid{position:absolute;left:0;top:795px;width:1200px;height:1383px}
.slide{position:absolute;width:382px;height:214px;overflow:hidden;background:#fff}
.c1{left:15px}.c2{left:409px}.c3{left:803px}
.r1{top:15px}.r2{top:242px}.r3{top:468px}.r4{top:695px}.r5{top:921px}.r6{top:1149px}
.photo{position:absolute;inset:0}
.photo.factory{background:radial-gradient(ellipse at 80% 60%,#6b5a2a 0%,#24343d 30%,transparent 60%),linear-gradient(100deg,#02070c 0%,#0a2233 55%,#183847 100%)}
.photo.brain{background:radial-gradient(circle at 68% 35%,#3aa6e8 0%,#114a78 18%,transparent 40%),linear-gradient(100deg,#02070c 0%,#071a2b 60%,#0b2a42 100%)}
.photo.tunnel{background:radial-gradient(ellipse at 50% 50%,#1f5a86 0%,#0b2a45 45%,#04111d 100%)}
.photo.hex{background:linear-gradient(180deg,#f4f6f8,#e6eaee)}
.photo.particles{background:radial-gradient(ellipse at 60% 60%,#12476e 0%,#07243b 50%,#03101b 100%)}
.photo.soft{background:linear-gradient(180deg,#fff,#eef1f4)}
.copyline{position:absolute;left:0;bottom:0;width:100%;height:11px;font-size:4.5px;letter-spacing:.5px;text-align:center;line-height:11px;color:#8fa0b0}
.copyline.dark{background:#202326}
.copyline.light{background:#fff;color:#9aa}
.logo{position:absolute;font-weight:500;color:var(--bright);letter-spacing:.3px}
.cover .logo{left:30px;top:33px;font-size:15px}
.cover h1{position:absolute;left:30px;top:78px;font-size:19px;line-height:21px;font-weight:700;color:var(--bright)}
.cover .sub{position:absolute;left:30px;top:124px;font-size:10.5px;font-weight:300;color:#d6dde4}
.pill{position:absolute;background:var(--blue);color:#fff;font-size:4.5px;font-weight:600;text-align:center;border-radius:1px}
.cover .pill{left:30px;top:158px;width:91px;height:12px;line-height:12px}
.cover.centered .logo{left:0;width:100%;text-align:center}
.cover.centered h1{left:0;width:100%;text-align:center;top:78px}
.cover.centered .sub{left:0;width:100%;text-align:center;top:125px}
.cover.centered .pill{left:146px;top:157px}
.footer .brand{position:absolute;left:12px;bottom:10px;font-size:9.5px;font-weight:500;color:var(--blue)}
.footer .bar{position:absolute;left:82px;right:30px;bottom:12px;height:7px;background:var(--blue)}
.footer .num{position:absolute;right:6px;bottom:12px;width:20px;height:7px;background:var(--sky);font-size:4px;color:#fff;text-align:center;line-height:7px}
.stitle{position:absolute;left:0;width:100%;top:15px;text-align:center;font-size:13.5px;font-weight:600;color:var(--ink)}
.tiny{font-size:4.6px;line-height:5.4px;color:#4a4f55}
.blue{color:var(--blue)}
.lbl{font-size:8.5px;line-height:9px;color:var(--blue);font-weight:400}
.abs{position:absolute}
.ring{position:absolute;width:31px;height:31px;border-radius:50%;border:1.4px solid var(--blue);background:#fff;display:flex;align-items:center;justify-content:center}
.disc{position:absolute;border-radius:50%;display:flex;align-items:center;justify-content:center}
.center{text-align:center}
.light-t{color:#dfe6ec}
</style>
</head>
<body>

<section class="hero">
  <div class="wordmark">Quelmoro</div>
  <div class="feature slide cover" style="width:760px;height:428px">
    <div class="photo factory" role="img" aria-label="Industrial robot arms welding with sparks in a dark factory"></div>
    <div class="logo" style="left:60px;top:70px;font-size:30px">Quelmoro</div>
    <h1 style="left:60px;top:150px;font-size:38px;line-height:42px;color:#fff">Presentation<br>Title Goes Here</h1>
    <div class="sub" style="left:60px;top:245px;font-size:20px;color:#e6ecf1">Subtitle of Presentation Goes Here!</div>
    <div class="pill" style="left:60px;top:315px;width:182px;height:26px;line-height:26px;font-size:10px">Sunday, January 16, 2022</div>
    <div class="copyline" style="height:24px;line-height:24px;font-size:9px;color:#aab6c0">Copyright © Quelmoro</div>
  </div>
</section>

<section class="grid">

  <!-- Row 1 -->
  <article class="slide cover c1 r1">
    <div class="photo brain" role="img" aria-label="Glowing blue brain above a circuit chip"></div>
    <div class="logo">Quelmoro</div>
    <h1>Presentation<br>Title Goes Here</h1>
    <div class="sub">Subtitle of Presentation Goes Here!</div>
    <div class="pill">Sunday, January 16, 2022</div>
    <div class="copyline light">Copyright © Quelmoro</div>
  </article>

  <article class="slide cover c2 r1">
    <div class="photo factory" role="img" aria-label="Robot arms working beside a control screen"></div>
    <div class="logo">Quelmoro</div>
    <h1>Presentation<br>Title Goes Here</h1>
    <div class="sub">Subtitle of Presentation Goes Here!</div>
    <div class="pill">Sunday, January 16, 2022</div>
    <div class="copyline dark">Copyright © Quelmoro</div>
  </article>

  <article class="slide cover c3 r1">
    <div class="photo factory" role="img" aria-label="Industrial robot arms welding with sparks"></div>
    <div class="logo">Quelmoro</div>
    <h1>Presentation<br>Title Goes Here</h1>
    <div class="sub">Subtitle of Presentation Goes Here!</div>
    <div class="pill">Sunday, January 16, 2022</div>
    <div class="copyline dark">Copyright © Quelmoro</div>
  </article>

  <!-- Row 2 -->
  <article class="slide cover centered c1 r2">
    <div class="photo tunnel" role="img" aria-label="Blue digital data tunnel"></div>
    <div class="logo">Quelmoro</div>
    <h1>Presentation Title<br>Goes Here</h1>
    <div class="sub">Subtitle of Presentation Goes Here!</div>
    <div class="pill">Sunday, January 16, 2022</div>
    <div class="copyline light">Copyright © Quelmoro</div>
  </article>

  <article class="slide cover centered c2 r2">
    <div class="photo hex" role="img" aria-label="Soft white hexagon texture"></div>
    <div class="logo">Quelmoro</div>
    <h1 style="color:var(--blue)">Presentation Title<br>Goes Here</h1>
    <div class="sub" style="color:#777">Subtitle of Presentation Goes Here!</div>
    <div class="pill">Sunday, January 16, 2022</div>
    <div class="copyline dark">Copyright © Quelmoro</div>
  </article>

  <article class="slide footer c3 r2">
    <div class="stitle">Agenda Slide</div>
    <div class="abs" style="left:52px;top:105px;font-size:12.5px;font-weight:600">Tópicos Hoy</div>
    <svg class="abs" style="left:150px;top:45px" width="70" height="135" viewBox="0 0 70 135">
      <path d="M2 4 Q68 20 68 67 Q68 114 2 130" fill="none" stroke="#cfd3d8" stroke-width="3"/>
    </svg>
    <div class="disc" style="left:174px;top:48px;width:13px;height:13px;background:var(--navy);color:#fff;font-size:6px">1</div>
    <div class="disc" style="left:204px;top:86px;width:13px;height:13px;background:var(--mist);color:#fff;font-size:6px">2</div>
    <div class="disc" style="left:204px;top:123px;width:13px;height:13px;background:#c8c8c8;color:#fff;font-size:6px">3</div>
    <div class="disc" style="left:174px;top:160px;width:13px;height:13px;background:#222;color:#fff;font-size:6px">4</div>
    <div class="abs" style="left:207px;top:47px"><div class="lbl" style="color:var(--blue)">Your Title Goes Here</div><div class="tiny">Your Subtitle Goes Here</div></div>
    <div class="abs" style="left:228px;top:84px"><div class="lbl" style="color:var(--sky)">Your Title Goes Here</div><div class="tiny">Your Subtitle Goes Here</div></div>
    <div class="abs" style="left:228px;top:121px"><div class="lbl" style="color:#999">Your Title Goes Here</div><div class="tiny">Your Subtitle Goes Here</div></div>
    <div class="abs" style="left:207px;top:157px"><div class="lbl" style="color:#333">Your Title Goes Here</div><div class="tiny">Your Subtitle Goes Here</div></div>
    <div class="brand">Quelmoro</div><div class="bar"></div><div class="num">6</div>
  </article>

  <!-- Row 3 -->
  <article class="slide footer c1 r3">
    <div class="photo hex" role="img" aria-label="Soft white hexagon texture"></div>
    <div class="stitle">About us</div>
    <div class="abs tiny center" style="left:28px;width:326px;top:40px;font-size:5.6px;line-height:6.4px">We are specialists in automation, process control, information technologies, development and consulting for quality, efficiency and production. Our goal is to always provide the best solutions in conjunction with our technology partners Fendaro.</div>
    <div class="ring" style="left:60px;top:78px"><svg width="13" height="13" viewBox="0 0 13 13"><rect x="3" y="3" width="7" height="7" fill="none" stroke="#0677BA"/><path d="M5 1v2M8 1v2M5 10v2M8 10v2M1 5h2M1 8h2M10 5h2M10 8h2" stroke="#0677BA"/></svg></div>
    <div class="ring" style="left:175px;top:78px"><svg width="13" height="13" viewBox="0 0 13 13"><path d="M6.5 1L12 4v5L6.5 12L1 9V4z M1 4l5.5 3L12 4 M6.5 7v5" fill="none" stroke="#0677BA"/></svg></div>
    <div class="ring" style="left:289px;top:78px"><svg width="13" height="13" viewBox="0 0 13 13"><circle cx="6.5" cy="6.5" r="5" fill="none" stroke="#0677BA"/><circle cx="6.5" cy="6.5" r="2" fill="none" stroke="#0677BA"/></svg></div>
    <div class="abs lbl center" style="left:18px;width:115px;top:116px">Smart<br>Machines</div>
    <div class="abs lbl center" style="left:133px;width:115px;top:116px">Operational<br>Excellence</div>
    <div class="abs lbl center" style="left:248px;width:115px;top:116px">Industrial<br>Internet</div>
    <div class="abs tiny center" style="left:26px;width:100px;top:139px">Intelligent machines in operation and control, in the same synchronization regardless of the brand installed. Efficiency that saves in operation.</div>
    <div class="abs tiny center" style="left:141px;width:100px;top:139px">Operational excellence is part of our language, strengthening the ties of efficiency in the company with every result we deliver.</div>
    <div class="abs tiny center" style="left:256px;width:100px;top:139px">Extending the Internet to industrial operation will exceed global energy savings by more than one billion. Be part of it.</div>
    <div class="brand">Quelmoro</div><div class="bar"></div><div class="num">7</div>
  </article>

  <article class="slide c2 r3">
    <div class="photo factory" role="img" aria-label="Industrial robot arms welding in a dark factory"></div>
    <div class="logo" style="left:35px;top:85px;font-size:11px">Quelmoro</div>
    <div class="abs" style="left:35px;top:122px;font-size:19px;font-weight:700;color:var(--bright)">Section Break</div>
    <div class="abs" style="left:35px;top:148px;width:210px;font-size:9px;line-height:10px;font-weight:300;color:#c3ccd4">Lorem ipsum dolor sit amet, consectetur adipiscing elit. Vivamus eu dui ex. Curabitur dapibus dignissim dui.</div>
  </article>

  <article class="slide footer c3 r3">
    <div class="stitle">Services</div>
    <div class="ring" style="left:155px;top:57px"><svg width="14" height="14" viewBox="0 0 14 14"><path d="M2 9V7a5 5 0 0 1 10 0v2" fill="none" stroke="#0677BA"/><rect x="1.5" y="8" width="2.5" height="4" fill="none" stroke="#0677BA"/><rect x="10" y="8" width="2.5" height="4" fill="none" stroke="#0677BA"/></svg></div>
    <div class="ring" style="left:193px;top:57px"><svg width="14" height="14" viewBox="0 0 14 14"><path d="M1 5l6-3 6 3-6 3z M4 7v3c2 2 4 2 6 0V7" fill="none" stroke="#0677BA"/></svg></div>
    <div class="ring" style="left:155px;top:97px"><svg width="14" height="14" viewBox="0 0 14 14"><rect x="2" y="2" width="10" height="7" fill="none" stroke="#0677BA"/><path d="M5 12h4M7 9v3" stroke="#0677BA"/></svg></div>
    <div class="ring" style="left:193px;top:97px"><svg width="14" height="14" viewBox="0 0 14 14"><path d="M3 1h6l3 3v9H3z M5 7h5M5 9.5h5" fill="none" stroke="#0677BA"/></svg></div>
    <div class="ring" style="left:155px;top:137px"><svg width="14" height="14" viewBox="0 0 14 14"><circle cx="7" cy="7" r="5.5" fill="none" stroke="#0677BA"/><path d="M1.5 7h11M7 1.5c-3 3.5-3 7.5 0 11M7 1.5c3 3.5 3 7.5 0 11" fill="none" stroke="#0677BA"/></svg></div>
    <div class="ring" style="left:193px;top:137px"><svg width="14" height="14" viewBox="0 0 14 14"><path d="M1 7l3-3 3 2 3-2 3 3-4 3-2-1-2 1z" fill="none" stroke="#0677BA"/></svg></div>
    <div class="abs" style="left:40px;width:108px;top:57px;text-align:right"><div class="lbl" style="font-size:7.5px">Tech Support</div><div class="tiny" style="font-size:4.2px">We provide solutions to any event, we have a team of experts in industrial automation.</div></div>
    <div class="abs" style="left:40px;width:108px;top:97px;text-align:right"><div class="lbl" style="font-size:7.5px">Tech Courses</div><div class="tiny" style="font-size:4.2px">We offer completely customized courses based on the need of our customers.</div></div>
    <div class="abs" style="left:40px;width:108px;top:137px;text-align:right"><div class="lbl" style="font-size:7.5px">Consultory</div><div class="tiny" style="font-size:4.2px">We offer the most advanced in industrial technology, hardware and software update.</div></div>
    <div class="abs" style="left:236px;width:100px;top:57px"><div class="lbl" style="font-size:7.5px">Certification</div><div class="tiny" style="font-size:4.2px">We offer official certifications based on the need of our customers.</div></div>
    <div class="abs" style="left:236px;width:100px;top:97px"><div class="lbl" style="font-size:7.5px">Diagnostics</div><div class="tiny" style="font-size:4.2px">We offer the most advanced in industrial technology, hardware and software update.</div></div>
    <div class="abs" style="left:236px;width:100px;top:137px"><div class="lbl" style="font-size:7.5px">Customer Attention</div><div class="tiny" style="font-size:4.2px">We offer the most advanced in industrial technology, hardware and software update.</div></div>
    <div class="brand">Quelmoro</div><div class="bar"></div><div class="num">9</div>
  </article>

  <!-- Row 4 -->
  <article class="slide footer c1 r4">
    <div class="photo" style="height:107px;background:linear-gradient(100deg,#1a2530 0%,#0b2233 50%,#102c3e 100%)" role="img" aria-label="Engineer in a hard hat working at an industrial control panel"></div>
    <div class="logo" style="left:0;width:100%;text-align:center;top:18px;font-size:11px;color:#fff">Quelmoro</div>
    <div class="abs" style="left:0;width:100%;text-align:center;top:47px;font-size:16px;font-weight:700;color:#fff">Industries We Serve</div>
    <div class="disc" style="left:29px;top:92px;width:30px;height:30px;background:var(--blue);border:2px solid #fff"><svg width="13" height="13" viewBox="0 0 13 13"><circle cx="3" cy="3" r="2" fill="none" stroke="#fff"/><circle cx="10" cy="4" r="2" fill="none" stroke="#fff"/><circle cx="6" cy="10" r="2" fill="none" stroke="#fff"/><path d="M4.5 4l4 0M3.8 4.8l1.6 3.6M9 5.7L7 8.5" stroke="#fff"/></svg></div>
    <div class="disc" style="left:102px;top:92px;width:30px;height:30px;background:var(--blue);border:2px solid #fff"><svg width="13" height="13" viewBox="0 0 13 13"><rect x="2" y="3" width="9" height="7" rx="1" fill="none" stroke="#fff"/><path d="M6.5 1v2M4 12h5" stroke="#fff"/></svg></div>
    <div class="disc" style="left:175px;top:92px;width:30px;height:30px;background:var(--blue);border:2px solid #fff"><svg width="13" height="13" viewBox="0 0 13 13"><rect x="3.5" y="1.5" width="6" height="10" fill="none" stroke="#fff"/><path d="M3.5 5h6" stroke="#fff"/></svg></div>
    <div class="disc" style="left:248px;top:92px;width:30px;height:30px;background:var(--blue);border:2px solid #fff"><svg width="13" height="13" viewBox="0 0 13 13"><path d="M1 11L11 2M4 11l8-6M1 8l6-6" stroke="#fff"/></svg></div>
    <div class="disc" style="left:321px;top:92px;width:30px;height:30px;background:var(--blue);border:2px solid #fff"><svg width="13" height="13" viewBox="0 0 13 13"><path d="M8 1L3 7h3.5L5 12l5-6H6.5z" fill="none" stroke="#fff"/></svg></div>
    <div class="abs lbl center" style="left:14px;width:60px;top:128px;font-size:7.5px;line-height:8px">Chemical<br>Industry</div>
    <div class="abs lbl center" style="left:87px;width:60px;top:128px;font-size:7.5px">Automotive</div>
    <div class="abs lbl center" style="left:160px;width:60px;top:128px;font-size:7.5px">Automotive</div>
    <div class="abs lbl center" style="left:233px;width:60px;top:128px;font-size:7.5px;line-height:8px">Mining And<br>Metals</div>
    <div class="abs lbl center" style="left:306px;width:60px;top:128px;font-size:7.5px">Energy</div>
    <div class="abs tiny center" style="left:14px;width:62px;top:148px;font-size:4px;line-height:4.8px">Lorem ipsum dolor sit amet, consectetur adipiscing elit. Vivamus eu dui ex. Curabitur dapibus dignissim dui.</div>
    <div class="abs tiny center" style="left:87px;width:62px;top:148px;font-size:4px;line-height:4.8px">Lorem ipsum dolor sit amet, consectetur adipiscing elit. Vivamus eu dui ex. Curabitur dapibus dignissim dui.</div>
    <div class="abs tiny center" style="left:160px;width:62px;top:148px;font-size:4px;line-height:4.8px">Lorem ipsum dolor sit amet, consectetur adipiscing elit. Vivamus eu dui ex. Curabitur dapibus dignissim dui.</div>
    <div class="abs tiny center" style="left:233px;width:62px;top:148px;font-size:4px;line-height:4.8px">Lorem ipsum dolor sit amet, consectetur adipiscing elit. Vivamus eu dui ex. Curabitur dapibus dignissim dui.</div>
    <div class="abs tiny center" style="left:306px;width:62px;top:148px;font-size:4px;line-height:4.8px">Lorem ipsum dolor sit amet, consectetur adipiscing elit. Vivamus eu dui ex. Curabitur dapibus dignissim dui.</div>
    <div class="brand">Quelmoro</div><div class="bar"></div><div class="num">10</div>
  </article>

  <article class="slide footer c2 r4">
    <div class="stitle">Slide Title Goes Here</div>
    <div class="disc" style="left:50px;top:57px;width:50px;height:50px;background:var(--blue)"><svg width="20" height="22" viewBox="0 0 20 22"><path d="M10 2a6 6 0 0 0-4 10.5V15h8v-2.5A6 6 0 0 0 10 2z M7 18h6" fill="none" stroke="#fff" stroke-width="1.6"/></svg></div>
    <div class="disc" style="left:166px;top:57px;width:50px;height:50px;background:var(--sky)"><svg width="22" height="20" viewBox="0 0 22 20"><rect x="3" y="3" width="16" height="10" fill="none" stroke="#fff" stroke-width="1.6"/><path d="M1 16h20" stroke="#fff" stroke-width="1.6"/></svg></div>
    <div class="disc" style="left:281px;top:57px;width:50px;height:50px;background:#8e9398"><svg width="24" height="16" viewBox="0 0 24 16"><path d="M6 14a4 4 0 0 1 0-8 6 6 0 0 1 11-1 4.5 4.5 0 0 1 1 9z" fill="#fff"/></svg></div>
    <div class="abs lbl center" style="left:15px;width:120px;top:115px;color:var(--blue)">Heading Goes Here</div>
    <div class="abs lbl center" style="left:131px;width:120px;top:115px;color:var(--sky)">Heading Goes Here</div>
    <div class="abs lbl center" style="left:246px;width:120px;top:115px;color:#8e9398">Heading Goes Here</div>
    <div class="abs tiny center" style="left:25px;width:100px;top:127px">Lorem ipsum dolor sit amet, consectetur adipiscing elit. Vivamus eu dui ex. Curabitur dapibus dignissim dui, in molestie metus feugiat sed. Duis eget tellus porta.</div>
    <div class="abs tiny center" style="left:141px;width:100px;top:127px">Lorem ipsum dolor sit amet, consectetur adipiscing elit. Vivamus eu dui ex. Curabitur dapibus dignissim dui, in molestie metus feugiat sed. Duis eget tellus porta.</div>
    <div class="abs tiny center" style="left:256px;width:100px;top:127px">Lorem ipsum dolor sit amet, consectetur adipiscing elit. Vivamus eu dui ex. Curabitur dapibus dignissim dui, in molestie metus feugiat sed. Duis eget tellus porta.</div>
    <div class="brand">Quelmoro</div><div class="bar"></div><div class="num">11</div>
  </article>

  <article class="slide footer c3 r4">
    <div class="stitle" style="font-size:12.5px">Uso de analytics en máquinas - Casos actuales</div>
    <div class="disc" style="left:12px;top:53px;width:54px;height:54px;background:radial-gradient(circle,#8a9097,#3a4450);border:2px solid var(--navy)" role="img" aria-label="Industrial cooling room machinery"></div>
    <div class="disc" style="left:193px;top:53px;width:54px;height:54px;background:radial-gradient(circle,#9aa1a8,#4b545d);border:2px solid var(--navy)" role="img" aria-label="Paint manufacturing line"></div>
    <div class="disc" style="left:12px;top:115px;width:54px;height:54px;background:radial-gradient(circle,#d98a2e,#2a3440);border:2px solid var(--navy)" role="img" aria-label="Cable manufacturing spool"></div>
    <div class="disc" style="left:193px;top:115px;width:54px;height:54px;background:radial-gradient(circle,#a8673a,#3d2e2a);border:2px solid var(--navy)" role="img" aria-label="Transformer core coils"></div>
    <div class="abs" style="left:72px;width:115px;top:57px"><div class="lbl" style="font-size:7.5px;line-height:7.5px">Ahorro energía en cuarto de máquinas.</div><div class="tiny" style="font-size:3.8px;line-height:4.4px">Generación agua fría para elaboración. Variable de predicción consumo energético y encendido de equipos.</div><div class="tiny blue" style="font-size:3.8px">12% costo de consumo energético</div></div>
    <div class="abs" style="left:253px;width:115px;top:57px"><div class="lbl" style="font-size:7.5px;line-height:7.5px">Ahorro en fabricación de pintura líquida.</div><div class="tiny" style="font-size:3.8px;line-height:4.4px">Control de receta de pintura automotriz. Instrucciones de llenado y tipo de producto digitalizadas por sistema.</div><div class="tiny blue" style="font-size:3.8px">ahorros de 30% costos de operación</div></div>
    <div class="abs" style="left:72px;width:115px;top:119px"><div class="lbl" style="font-size:7.5px;line-height:7.5px">Mantenimiento predictivo fabricación cables.</div><div class="tiny" style="font-size:3.8px;line-height:4.4px">Digitalización de máquinas de elaboración de cable. Control de disponibilidad y tiempo de paro.</div><div class="tiny blue" style="font-size:3.8px">Predicción falla al 87%. Ahorros operativos de 15%</div></div>
    <div class="abs" style="left:253px;width:115px;top:119px"><div class="lbl" style="font-size:7.5px;line-height:7.5px">Modelo predictivo hornos para núcleos transformadores.</div><div class="tiny" style="font-size:3.8px;line-height:4.4px">Digitalización de variables que afectan la humedad en núcleos para transformadores.</div><div class="tiny blue" style="font-size:3.8px">materiales del 1% y 25% en disponibilidad</div></div>
    <div class="brand">Quelmoro</div><div class="bar"></div><div class="num">12</div>
  </article>

  <!-- Row 5 -->
  <article class="slide footer c1 r5">
    <div class="photo" style="height:107px;background:linear-gradient(100deg,#3a2418 0%,#14212c 35%,#0b2233 70%,#1d3440 100%)" role="img" aria-label="Technician in safety gear beside robotic equipment"></div>
    <div class="logo" style="left:0;width:100%;text-align:center;top:20px;font-size:9px;color:#fff">Quelmoro</div>
    <div class="abs" style="left:0;width:100%;text-align:center;top:45px;font-size:16px;font-weight:700;color:#fff">Expositors</div>
    <div class="disc" style="left:51px;top:81px;width:52px;height:52px;background:var(--blue);border:2px solid #fff"><svg width="22" height="22" viewBox="0 0 22 22"><circle cx="11" cy="9" r="6" fill="#fff"/><path d="M7 14l-2 7 6-3 6 3-2-7" fill="#fff"/></svg></div>
    <div class="disc" style="left:165px;top:81px;width:52px;height:52px;background:var(--sky);border:2px solid #fff"><svg width="22" height="22" viewBox="0 0 22 22"><path d="M6 3h10v5a5 5 0 0 1-10 0z M9 14h4v3H9z M6 19h10" fill="#fff" stroke="#fff"/></svg></div>
    <div class="disc" style="left:280px;top:81px;width:52px;height:52px;background:#8e9398;border:2px solid #fff"><svg width="22" height="22" viewBox="0 0 22 22"><path d="M3 19h16M5 17v-5h3v5M10 17v-8h3v8M15 17V6h3v11" fill="#fff" stroke="#fff"/></svg></div>
    <div class="abs lbl center" style="left:17px;width:120px;top:142px;color:var(--blue)">Your Heading<br>Goes Here</div>
    <div class="abs lbl center" style="left:131px;width:120px;top:142px;color:var(--sky)">Your Heading<br>Goes Here</div>
    <div class="abs lbl center" style="left:246px;width:120px;top:142px;color:#8e9398">Your Heading<br>Goes Here</div>
    <div class="brand">Quelmoro</div><div class="bar"></div><div class="num">13</div>
  </article>

  <article class="slide footer c2 r5">
    <div class="stitle">Column Slide</div>
    <div class="abs" style="left:24px;width:160px;top:58px">
      <div class="lbl" style="font-weight:700;font-size:8px">Heading Goes Here</div>
      <ul class="tiny" style="margin-top:6px;padding-left:8px;list-style:'•  ';color:#4a4f55">
        <li style="margin-bottom:3px">Lorem ipsum dolor sit amet, consectetur adipiscing elit. Vivamus eu dui ex.</li>
        <li style="margin-bottom:3px">Curabitur dapibus dignissim dui, in molestie metus feugiat sed. Praesent aliquet lorem ex.</li>
        <li style="margin-bottom:3px">Lorem ipsum dolor sit amet, consectetur adipiscing elit. Vivamus eu dui ex. Curabitur dapibus dignissim dui.</li>
        <li style="margin-bottom:3px">Lorem ipsum dolor sit amet, consectetur adipiscing elit. Vivamus eu dui ex.</li>
        <li>Praesent aliquet lorem ex, eu dapibus odio varius at. Duis eget tellus porta.</li>
      </ul>
    </div>
    <div class="abs" style="left:200px;width:160px;top:58px">
      <div class="lbl" style="font-weight:700;font-size:8px">Heading Goes Here</div>
      <ul class="tiny" style="margin-top:6px;padding-left:8px;list-style:'•  ';color:#4a4f55">
        <li style="margin-bottom:3px">Lorem ipsum dolor sit amet, consectetur adipiscing elit. Vivamus eu dui ex.</li>
        <li style="margin-bottom:3px">Curabitur dapibus dignissim dui, in molestie metus feugiat sed. Praesent aliquet lorem ex.</li>
        <li style="margin-bottom:3px">Lorem ipsum dolor sit amet, consectetur adipiscing elit. Vivamus eu dui ex. Curabitur dapibus dignissim dui.</li>
        <li style="margin-bottom:3px">Lorem ipsum dolor sit amet, consectetur adipiscing elit. Vivamus eu dui ex.</li>
        <li>Praesent aliquet lorem ex, eu dapibus odio varius at. Duis eget tellus porta.</li>
      </ul>
    </div>
    <div class="brand">Quelmoro</div><div class="bar"></div><div class="num">14</div>
  </article>

  <article class="slide footer c3 r5">
    <div class="photo factory" role="img" aria-label="Industrial robot arms in a dark factory"></div>
    <div class="abs" style="left:39px;top:45px;font-size:13.5px;font-weight:700;color:var(--bright)">Slide Title Goes Here</div>
    <div class="abs" style="left:39px;top:62px;font-size:7px;color:#fff">Subtitle Goes Here!</div>
    <div class="abs light-t" style="left:39px;top:78px;width:155px;font-size:5.4px;line-height:6.2px">
      <p style="margin-bottom:4px">Lorem ipsum dolor sit amet, consectetur adipiscing elit. Vivamus eu dui ex.</p>
      <p style="margin-bottom:4px">Curabitur dapibus dignissim dui, in molestie metus feugiat sed. Praesent aliquet lorem ex, eu dapibus odio varius. Lorem ipsum dolor sit amet, consectetur adipiscing elit. Vivamus eu dui ex. Curabitur dapibus dignissim dui, in molestie metus feugiat sed.</p>
      <p>Lorem ipsum dolor sit amet, consectetur adipiscing elit. Vivamus eu dui ex. Curabitur dapibus dignissim dui, in molestie metus feugiat sed.</p>
    </div>
    <div class="brand">Quelmoro</div><div class="bar"></div><div class="num">15</div>
  </article>

  <!-- Row 6 -->
  <article class="slide footer c1 r6">
    <div class="stitle">Map Slide Title Goes Here</div>
    <div class="abs" style="left:150px;top:48px;width:215px;height:130px;background:radial-gradient(ellipse at 50% 50%,#e6e9ec 0%,#f3f5f7 60%,#fff 100%)" role="img" aria-label="Faint grey world map"></div>
    <div class="abs" style="left:24px;width:110px;top:57px"><div class="lbl" style="font-size:7.5px">Heading Goes Here</div><div class="tiny" style="font-size:4.2px;line-height:5px;margin-top:2px">Lorem ipsum dolor sit amet, consectetur adipiscing elit. Vivamus eu dui ex. Curabitur dapibus dignissim dui.</div></div>
    <div class="abs" style="left:24px;width:110px;top:97px"><div class="lbl" style="font-size:7.5px">Heading Goes Here</div><div class="tiny" style="font-size:4.2px;line-height:5px;margin-top:2px">Lorem ipsum dolor sit amet, consectetur adipiscing elit. Vivamus eu dui ex. Curabitur dapibus dignissim dui.</div></div>
    <div class="abs" style="left:24px;width:110px;top:137px"><div class="lbl" style="font-size:7.5px">Heading Goes Here</div><div class="tiny" style="font-size:4.2px;line-height:5px;margin-top:2px">Lorem ipsum dolor sit amet, consectetur adipiscing elit. Vivamus eu dui ex. Curabitur dapibus dignissim dui.</div></div>
    <div class="brand">Quelmoro</div><div class="bar"></div><div class="num">16</div>
  </article>

  <article class="slide c2 r6">
    <div class="photo factory" role="img" aria-label="Industrial robot arms in a dark factory"></div>
    <div class="logo" style="left:37px;top:58px;font-size:14px">Quelmoro</div>
    <div class="abs" style="left:37px;top:90px;font-size:9px;color:#fff">Contact Us</div>
    <div class="abs" style="left:37px;top:103px;font-size:4.6px;line-height:5.4px;color:#e0e6ea">Av. Lomas Altas #218, Vistaluz,<br>64120 Ciudad Norte</div>
    <div class="abs" style="left:37px;top:122px;font-size:4.6px;line-height:10px;color:#e0e6ea">
      <div><svg width="6" height="6" viewBox="0 0 6 6"><path d="M1 0.5l1.2 1.5-0.7 0.8a4 4 0 0 0 1.7 1.7l0.8-0.7 1.5 1.2-0.8 0.8C2.5 5.6 0.4 3.5 0.2 1.3z" fill="#fff"/></svg>&nbsp; 81 5550 2417</div>
      <div><svg width="6" height="6" viewBox="0 0 6 6"><circle cx="3" cy="3" r="2.4" fill="none" stroke="#fff" stroke-width=".7"/><circle cx="3" cy="3" r="1" fill="none" stroke="#fff" stroke-width=".7"/></svg>&nbsp; informes@quelmoro-mx.com</div>
      <div><svg width="6" height="6" viewBox="0 0 6 6"><circle cx="3" cy="3" r="2.5" fill="none" stroke="#fff" stroke-width=".6"/><path d="M0.5 3h5M3 0.5v5" stroke="#fff" stroke-width=".5"/></svg>&nbsp; www.quelmoro-mx.com</div>
    </div>
    <div class="copyline light">Copyright © Quelmoro</div>
  </article>

  <article class="slide c3 r6">
    <div class="photo particles" role="img" aria-label="Blue digital particles on a dark background"></div>
    <div class="logo" style="left:37px;top:58px;font-size:14px">Quelmoro</div>
    <div class="abs" style="left:37px;top:90px;font-size:9px;color:#fff">Contact Us</div>
    <div class="abs" style="left:37px;top:103px;font-size:4.6px;line-height:5.4px;color:#e0e6ea">Av. Lomas Altas #218, Vistaluz,<br>64120 Ciudad Norte</div>
    <div class="abs" style="left:37px;top:122px;font-size:4.6px;line-height:10px;color:#e0e6ea">
      <div><svg width="6" height="6" viewBox="0 0 6 6"><path d="M1 0.5l1.2 1.5-0.7 0.8a4 4 0 0 0 1.7 1.7l0.8-0.7 1.5 1.2-0.8 0.8C2.5 5.6 0.4 3.5 0.2 1.3z" fill="#2a8fd8"/></svg>&nbsp; 81 5550 2417</div>
      <div><svg width="6" height="6" viewBox="0 0 6 6"><circle cx="3" cy="3" r="2.4" fill="none" stroke="#2a8fd8" stroke-width=".7"/><circle cx="3" cy="3" r="1" fill="none" stroke="#2a8fd8" stroke-width=".7"/></svg>&nbsp; informes@quelmoro-mx.com</div>
      <div><svg width="6" height="6" viewBox="0 0 6 6"><circle cx="3" cy="3" r="2.5" fill="none" stroke="#2a8fd8" stroke-width=".6"/><path d="M0.5 3h5M3 0.5v5" stroke="#2a8fd8" stroke-width=".5"/></svg>&nbsp; www.quelmoro-mx.com</div>
    </div>
    <div class="copyline light">Copyright © Quelmoro</div>
  </article>

</section>
</body>
</html>
```